Design a double sided business card

We are looking for a clean, eye-catching, and contemporary design that enhances the brand and presents a premium, professional image. Our preference is for a brown card with black gloss detailing and embossed elements; however, we are open to creative input and design suggestions that best achieve a strong visual impact.

Please see the attached existing business card for reference. We use both black and brown colours consistently across our branding.

On sample provided

```html
<!DOCTYPE html>
<html lang="en">
<head>
<meta charset="utf-8">
<title>Halden – Business Card</title>
<link href="https://fonts.googleapis.com/css2?family=Poppins:wght@400;500;600;700&display=swap" rel="stylesheet">
<style>
  :root {
    --page-bg: #8a8a8c;
    --card-black: #000000;
    --tan: #cdb69b;
    --tan-light: #e6d8c6;
    --tan-deep: #b89f7d;
    --ink: #0b0b0b;
  }
  html, body {
    margin: 0;
    padding: 0;
    width: 900px;
    height: 1200px;
    overflow: hidden;
    background: var(--page-bg);
    font-family: "Poppins", sans-serif;
  }
  .canvas {
    position: relative;
    width: 900px;
    height: 1200px;
  }
  .card {
    position: absolute;
    left: 149px;
    width: 601px;
  }
  .card--front {
    top: 168px;
    height: 386px;
    overflow: hidden;
  }
  .front-texture {
    position: absolute;
    inset: 0;
    background: linear-gradient(90deg, var(--tan-deep) 0%, var(--tan) 55%, var(--tan-light) 100%);
  }
  .front-wordmark {
    position: absolute;
    left: 0;
    right: 0;
    top: 168px;
    text-align: center;
    margin: 0;
    font-weight: 700;
    font-size: 52px;
    letter-spacing: 6px;
    line-height: 1;
    color: var(--ink);
  }
  .card--back {
    top: 644px;
    height: 388px;
    background: var(--card-black);
    color: var(--tan);
  }
  .brand-block {
    position: absolute;
    left: 44px;
    top: 118px;
    width: 168px;
    text-align: center;
  }
  .brand-square {
    display: block;
    width: 72px;
    height: 72px;
    margin: 0 auto 22px;
    border: 6px solid var(--tan);
    box-sizing: border-box;
  }
  .brand-name {
    margin: 0;
    font-weight: 600;
    font-size: 30px;
    letter-spacing: 4px;
    line-height: 1;
  }
  .divider {
    position: absolute;
    left: 325px;
    top: 93px;
    width: 2px;
    height: 203px;
    background: var(--tan);
  }
  .contact {
    position: absolute;
    left: 346px;
    top: 92px;
    width: 240px;
  }
  .contact-name {
    margin: 0;
    font-weight: 600;
    font-size: 22px;
    letter-spacing: 0.5px;
    line-height: 1.2;
  }
  .contact-role {
    margin: 2px 0 14px;
    font-size: 13px;
    letter-spacing: 1px;
    line-height: 1.3;
  }
  .contact-address {
    margin: 0 0 12px;
    font-size: 14.5px;
    line-height: 23px;
    font-style: normal;
    letter-spacing: 0.3px;
  }
  .contact-list {
    list-style: none;
    margin: 0;
    padding: 0;
    font-size: 14.5px;
    letter-spacing: 0.5px;
  }
  .contact-list li {
    display: flex;
    align-items: center;
    gap: 4px;
    height: 24px;
  }
  .contact-list svg {
    width: 12px;
    height: 12px;
    flex: none;
    fill: var(--tan);
  }
</style>
</head>
<body>
<div class="canvas">

  <section class="card card--front">
    <div class="front-texture" role="img" aria-label="Embossed repeating brand-mark pattern in brown tones"></div>
    <h1 class="front-wordmark">HALDEN</h1>
  </section>

  <section class="card card--back">
    <div class="brand-block">
      <span class="brand-square" aria-hidden="true"></span>
      <p class="brand-name">HALDEN</p>
    </div>

    <div class="divider" aria-hidden="true"></div>

    <div class="contact">
      <h2 class="contact-name">RAVI MEHTA</h2>
      <p class="contact-role">DIRECTOR</p>
      <address class="contact-address">The Meadow Hawthorn Lane<br>Eastbrook UB9 4PL</address>
      <ul class="contact-list">
        <li>
          <svg viewBox="0 0 24 24" aria-hidden="true"><path d="M6.6 10.8a15.1 15.1 0 0 0 6.6 6.6l2.2-2.2a1 1 0 0 1 1-.25 11.4 11.4 0 0 0 3.6.57 1 1 0 0 1 1 1V20a1 1 0 0 1-1 1A17 17 0 0 1 3 4a1 1 0 0 1 1-1h3.5a1 1 0 0 1 1 1c0 1.25.2 2.45.57 3.6a1 1 0 0 1-.25 1z"/></svg>
          0800 456 2210
        </li>
        <li>
          <svg viewBox="0 0 24 24" aria-hidden="true"><path d="M7 1h10a2 2 0 0 1 2 2v18a2 2 0 0 1-2 2H7a2 2 0 0 1-2-2V3a2 2 0 0 1 2-2zm0 3v15h10V4zm5 16a1 1 0 1 0 0 2 1 1 0 0 0 0-2z"/></svg>
          07700900321
        </li>
        <li>
          <svg viewBox="0 0 24 24" aria-hidden="true"><path d="M2 5h20v14H2zm2 2v.5l8 5 8-5V7zm0 2.9V17h16V9.9l-8 5z"/></svg>
          ravi@halden.co.uk
        </li>
        <li>
          <svg viewBox="0 0 24 24" aria-hidden="true"><path d="M12 2a10 10 0 1 0 0 20 10 10 0 0 0 0-20zm6.9 9h-3a15 15 0 0 0-1.3-6 8 8 0 0 1 4.3 6zM12 4c.9 1.2 1.7 3.8 1.9 7h-3.8c.2-3.2 1-5.8 1.9-7zM9.4 5a15 15 0 0 0-1.3 6h-3A8 8 0 0 1 9.4 5zM5.1 13h3a15 15 0 0 0 1.3 6 8 8 0 0 1-4.3-6zM12 20c-.9-1.2-1.7-3.8-1.9-7h3.8c-.2 3.2-1 5.8-1.9 7zm2.6-1a15 15 0 0 0 1.3-6h3a8 8 0 0 1-4.3 6z"/></svg>
          www.halden.co.uk
        </li>
      </ul>
    </div>
  </section>

</div>
</body>
</html>
```